Roll Up "RUNEN RIKA" for TV Studio Production

The RollUp has the size 100x200 cm (excluding margins). The goal is to have the four elements in capitals (wands, coins, swords, cups) as vector graphics with the "champagne and limousines" font, on the rollup, as well as my logo, all fitting together perfectly on the dark blue background of my logo. You should take the elements from the given pixfundus picture, put them on the card-frame of my Logo-tarot-card. The writing should be in German though! Here is the translation: Swords = Swords, Cups = Chalices, Wands = Wands, Pentacles = Coins. If you want to add information, then add:

FILMWELLE @RunenRika
runenmitrika@velmora.example
KLICKBAUM.EXAMPLE/RikaHolbeck

Good luck!

Target Market(s)

TV audience, mainly women between age 40 and 70 in Austria, Germany and Switzerland

Industry/Entity Type

Tarot Card Readings

Font styles to use
Other font styles liked:
• Champagne & Limousines (given data)

Colors
0054AA
0677BA
7BADD7
CADEEF
E8F1F8
0094D4
00A9DD
6FCCEA
C7EBF8
E9F6FB
00AB8E
00BBA5
67D7C9
C6EFE9
E9F9F6

Requirements
Must have
• MARGINS!! And the given Corporate Identity (Champagne font, my Logo colors etc.)
Nice to have
• Ready to print, with margins
Should not have
• please use the 5-pointed-star given in the briefing (not the pentagram) for the coins - thank you

```html
<!DOCTYPE html>
<html lang="de">
<head>
<meta charset="utf-8">
<title>Runen Rika – Roll-up</title>
<link rel="stylesheet" href="https://fonts.googleapis.com/css2?family=Josefin+Sans:wght@300&display=swap">
<style>
  :root {
    --stage: #e9ecea;
    --night: #07002c;
    --cyan: #1aaaf2;
    --violet: #6c6cf2;
    --title: #1cb4f5;
    --star: #1e9cf4;
    --art-top: rgba(30, 150, 240, 0.35);
    --art-bottom: rgba(108, 108, 242, 0.35);
  }
  * { box-sizing: border-box; margin: 0; padding: 0; }
  html, body {
    width: 982px;
    height: 1200px;
    overflow: hidden;
    background: var(--stage);
  }
  .rollup {
    position: absolute;
    left: 196px;
    top: 0;
    width: 590px;
    height: 1200px;
    background: var(--night);
    font-family: "Josefin Sans", sans-serif;
    font-weight: 300;
    color: var(--title);
  }
  .sky {
    position: absolute;
    inset: 0;
    width: 100%;
    height: 100%;
  }
  .sky .star { fill: var(--star); }
  .sky .sparkle { stroke: var(--star); stroke-width: 2; fill: none; }
  .sky .sparkle-core { fill: var(--star); }
  .brand-word {
    position: absolute;
    left: 0;
    width: 100%;
    text-align: center;
    font-family: "Josefin Sans", sans-serif;
    font-weight: 300;
    font-size: 74px;
    line-height: 1;
    letter-spacing: -1px;
  }
  .brand-word--top { top: 36px; }
  .brand-word--bottom { top: 346px; }
  .brand-mark {
    position: absolute;
    left: 225px;
    top: 152px;
    width: 140px;
    height: 140px;
    border: 2px solid var(--violet);
  }
  .card {
    position: absolute;
    width: 238px;
    height: 321px;
  }
  .card--wands { left: 43px; top: 450px; }
  .card--coins { left: 309px; top: 450px; }
  .card--chalices { left: 43px; top: 801px; }
  .card--swords { left: 309px; top: 796px; }
  .card-frame {
    position: absolute;
    inset: 0;
    width: 100%;
    height: 100%;
  }
  .card-title {
    position: absolute;
    top: 58px;
    left: 0;
    width: 100%;
    text-align: center;
    font-weight: 300;
    font-size: 37px;
    line-height: 1;
    color: var(--title);
  }
  .card-art {
    position: absolute;
    left: 18px;
    top: 104px;
    width: 202px;
    height: 192px;
    border-radius: 6px;
    background: linear-gradient(180deg, var(--art-top), var(--art-bottom));
  }
  .gradient-defs { position: absolute; width: 0; height: 0; }
</style>
</head>
<body>
<svg class="gradient-defs" aria-hidden="true">
  <defs>
    <linearGradient id="frame-gradient" x1="0" y1="0" x2="0" y2="1">
      <stop offset="0" stop-color="#1aaaf2"/>
      <stop offset="1" stop-color="#6c6cf2"/>
    </linearGradient>
    <path id="four-point-star" d="M0,-10 Q1.6,-1.6 10,0 Q1.6,1.6 0,10 Q-1.6,1.6 -10,0 Q-1.6,-1.6 0,-10 Z"/>
    <g id="sun-sparkle">
      <circle cx="0" cy="0" r="4"/>
      <path d="M0,-14 V-5 M0,5 V14 M-14,0 H-5 M5,0 H14 M-8,-8 L-3,-3 M3,3 L8,8 M-8,8 L-3,3 M3,-3 L8,-8"/>
    </g>
  </defs>
</svg>

<main class="rollup">
  <svg class="sky" viewBox="0 0 590 1200" aria-hidden="true">
    <g class="star">
      <use href="#four-point-star" transform="translate(532 43) scale(1.2)"/>
      <use href="#four-point-star" transform="translate(112 114) rotate(20) scale(0.8)"/>
      <use href="#four-point-star" transform="translate(55 191) scale(0.7)"/>
      <use href="#four-point-star" transform="translate(135 225) scale(0.9)"/>
      <use href="#four-point-star" transform="translate(86 374) scale(1.9)"/>
      <use href="#four-point-star" transform="translate(548 390) rotate(20) scale(1)"/>
      <use href="#four-point-star" transform="translate(32 1154) scale(0.7)"/>
      <use href="#four-point-star" transform="translate(545 1148) rotate(20) scale(1)"/>
    </g>
    <g class="sparkle">
      <use href="#sun-sparkle" transform="translate(487 142) scale(1.3)"/>
      <use href="#sun-sparkle" transform="translate(279 1156) scale(1.4)"/>
    </g>
    <g class="sparkle-core">
      <circle cx="76" cy="43" r="7"/>
      <circle cx="476" cy="289" r="8"/>
    </g>
    <g class="sparkle">
      <path d="M60,27 L92,59 M60,59 L92,27 M76,25 V61 M58,43 H94" stroke-width="1"/>
      <path d="M456,269 L496,309 M456,309 L496,269 M476,265 V313 M452,289 H500" stroke-width="1"/>
    </g>
  </svg>

  <h1 class="brand-word brand-word--top">RUNEN</h1>
  <div class="brand-mark" aria-hidden="true"></div>
  <p class="brand-word brand-word--bottom">RIKA</p>

  <section class="card card--wands">
    <svg class="card-frame" viewBox="0 0 238 321" aria-hidden="true">
      <g fill="none" stroke="url(#frame-gradient)">
        <rect x="1.5" y="1.5" width="235" height="318" rx="16" stroke-width="2.6"/>
        <rect x="10" y="10" width="218" height="301" stroke-width="1.2"/>
        <rect x="13" y="13" width="6" height="6" stroke-width="1"/>
        <rect x="219" y="13" width="6" height="6" stroke-width="1"/>
        <rect x="13" y="302" width="6" height="6" stroke-width="1"/>
        <rect x="219" y="302" width="6" height="6" stroke-width="1"/>
      </g>
    </svg>
    <h2 class="card-title">WANDS</h2>
    <div class="card-art" role="img" aria-label="Illustration: Zauberstab auf Sockel zwischen Lorbeerzweigen und Sternen"></div>
  </section>

  <section class="card card--coins">
    <svg class="card-frame" viewBox="0 0 238 321" aria-hidden="true">
      <g fill="none" stroke="url(#frame-gradient)">
        <rect x="1.5" y="1.5" width="235" height="318" rx="16" stroke-width="2.6"/>
        <rect x="10" y="10" width="218" height="301" stroke-width="1.2"/>
        <rect x="13" y="13" width="6" height="6" stroke-width="1"/>
        <rect x="219" y="13" width="6" height="6" stroke-width="1"/>
        <rect x="13" y="302" width="6" height="6" stroke-width="1"/>
        <rect x="219" y="302" width="6" height="6" stroke-width="1"/>
      </g>
    </svg>
    <h2 class="card-title">COINS</h2>
    <div class="card-art" role="img" aria-label="Illustration: Münze mit fünfzackigem Stern auf Sockel zwischen Lorbeerzweigen"></div>
  </section>

  <section class="card card--chalices">
    <svg class="card-frame" viewBox="0 0 238 321" aria-hidden="true">
      <g fill="none" stroke="url(#frame-gradient)">
        <rect x="1.5" y="1.5" width="235" height="318" rx="16" stroke-width="2.6"/>
        <rect x="10" y="10" width="218" height="301" stroke-width="1.2"/>
        <rect x="13" y="13" width="6" height="6" stroke-width="1"/>
        <rect x="219" y="13" width="6" height="6" stroke-width="1"/>
        <rect x="13" y="302" width="6" height="6" stroke-width="1"/>
        <rect x="219" y="302" width="6" height="6" stroke-width="1"/>
      </g>
    </svg>
    <h2 class="card-title">CHALICES</h2>
    <div class="card-art" role="img" aria-label="Illustration: Kristallkelch auf Sockel zwischen Lorbeerzweigen"></div>
  </section>

  <section class="card card--swords">
    <svg class="card-frame" viewBox="0 0 238 321" aria-hidden="true">
      <g fill="none" stroke="url(#frame-gradient)">
        <rect x="1.5" y="1.5" width="235" height="318" rx="16" stroke-width="2.6"/>
        <rect x="10" y="10" width="218" height="301" stroke-width="1.2"/>
        <rect x="13" y="13" width="6" height="6" stroke-width="1"/>
        <rect x="219" y="13" width="6" height="6" stroke-width="1"/>
        <rect x="13" y="302" width="6" height="6" stroke-width="1"/>
        <rect x="219" y="302" width="6" height="6" stroke-width="1"/>
      </g>
    </svg>
    <h2 class="card-title">SWORDS</h2>
    <div class="card-art" role="img" aria-label="Illustration: Dolch auf Sockel zwischen Lorbeerzweigen und Sternen"></div>
  </section>
</main>
</body>
</html>
```